Website Re-design and extension of an existing website

I have a Wordpress website currently and I need it to be upgraded. I have MOST of the content to get it started and the rest (video's, pictures ect) are on the way. I want to know if it is possible to convert my existing website into a Personal Brand website with a public speaking emphasis. I would like to have my website modeled after the following website:

http://www.vandolake.example/

I have attached a document entitled "Website Outline & Content" that has all of the text on it and it has red headlines that indicate where something needs to be added or designed. I will be happy to give more detail if needed.

Things I still need to get to you in order to design the website;

-Demo video
-Full length public speaking video

Target Market(s)

Corporations, universities, trade associations, private events

Coding

Coded - Design and coding required

Requirements
Must have
• Pictures, links, downloadable forms, MULTIPLE video's embedded, my logo, keep the colors in sync with my existing marketing material
Nice to have
• I would like my design colors thematic as already inherent in my marketing materials (see my Speaker One Sheet)

```html
<!DOCTYPE html>
<html lang="en">
<head>
<meta charset="utf-8">
<title>Cole Brandt — Holistic Health Speaker</title>
<link rel="stylesheet" href="https://fonts.googleapis.com/css2?family=Open+Sans:wght@400;600;700;800&display=swap">
<style>
:root{
  --olive:#5e6234;
  --olive-light:#8f8c55;
  --gold:#9a9459;
  --gold-text:#8c8a4e;
  --ink:#2e2e2e;
  --body:#555;
  --muted:#888;
  --band:#3a3a3a;
  --footer:#2b2b2b;
  --footer-bottom:#1f1f1f;
  --panel:#efefef;
  --card:#f2f2f2;
  --white:#fff;
}
*{box-sizing:border-box;margin:0;padding:0}
html,body{width:1200px;height:2493px;overflow:hidden}
body{font-family:"Open Sans",Arial,sans-serif;color:var(--body);background:var(--white);position:relative}
.abs{position:absolute}
.header{top:0;left:0;width:1200px;height:106px}
.brand{left:133px;top:25px;display:flex;align-items:center;gap:12px}
.brand-mark{width:56px;height:56px;border-radius:50%;background:var(--olive-light)}
.brand-name{font-size:34px;font-weight:800;color:var(--olive-light);line-height:1}
.connect{right:133px;top:38px;display:flex;align-items:center;gap:10px;font-size:13px;color:var(--muted)}
.social{width:32px;height:32px;border-radius:50%;background:#b8b8b8;display:inline-block}
.nav{top:106px;left:0;width:1200px;height:40px;background:var(--olive)}
.nav ul{list-style:none;display:flex;position:absolute;left:133px;top:0;height:40px}
.nav li{color:#fff;font-size:12.5px;line-height:40px;padding:0 11.5px}
.nav li.active{background:var(--olive-light)}
.hero{top:146px;left:0;width:1200px;height:469px;background:linear-gradient(90deg,#c9ccd2 0%,#dfe1e6 40%,#ececf0 60%,#ececf0 100%)}
.hero-photo{left:0;top:0;width:700px;height:469px;background:linear-gradient(120deg,#d6d7dc 0%,#b9bcc3 50%,#e6e6ea 100%)}
.arrow-tab{width:22px;height:34px;background:rgba(90,90,90,.5);top:220px}
.hero-copy{left:706px;top:12px;width:361px;text-align:center}
.hero-title{font-size:44px;font-weight:800;color:var(--gold-text);line-height:1.1}
.hero-sub{font-size:11.5px;color:var(--ink);white-space:nowrap}
.hero-lead{font-size:16.5px;font-weight:700;color:var(--ink);line-height:1.4;margin-top:6px}
.downloads{display:flex;gap:4px;margin-top:8px}
.dl{flex:1;background:var(--gold);color:#fff;padding:6px 4px;height:62px}
.dl b{display:block;font-size:15px;font-weight:800}
.dl span{font-size:10px;line-height:1.2;display:block}
.hero-text{font-size:10px;line-height:1.55;color:var(--ink);text-align:justify;margin-top:10px}
.hero-cta{display:block;border:1px solid var(--ink);margin-top:22px;padding:13px 0;font-size:12.5px;color:var(--ink);background:rgba(255,255,255,.3)}
.sugar{left:429px;top:223px;width:254px;background:rgba(255,255,255,.9)}
.sugar h2{font-size:25px;font-weight:700;color:var(--gold-text);padding:14px 18px 6px}
.sugar ul{padding:0 18px 12px 30px;font-size:14px;color:var(--ink);line-height:1.6}
.sugar .foot{background:var(--band);color:#fff;font-size:13px;font-weight:700;padding:12px 18px;line-height:1.4}
.optin{top:615px;left:0;width:1200px;height:160px;background:var(--band)}
.book{left:133px;top:10px;width:96px;height:143px;background:linear-gradient(#e8d98a,#c49a3a)}
.optin h3{position:absolute;left:258px;top:15px;width:812px;font-size:21px;font-weight:700;color:#ddd;line-height:1.35}
.optin form{position:absolute;left:258px;top:88px;display:flex}
.optin .email{width:322px;height:45px;background:#fff;font-size:14px;color:#444;padding:13px 18px}
.optin .subscribe{width:113px;height:45px;background:var(--gold);color:var(--ink);font-weight:800;font-size:15px;text-align:center;line-height:45px}
.about{top:775px;left:0;width:1200px;height:393px}
.about h2{position:absolute;left:133px;top:72px;font-size:23px;font-weight:600;color:var(--ink)}
.about p{position:absolute;left:133px;top:114px;width:450px;font-size:12px;line-height:20px;height:160px;overflow:hidden}
.btn{background:var(--gold);color:var(--ink);font-weight:700;font-size:13px;text-align:center}
.about .btn{position:absolute;left:133px;top:278px;width:118px;height:36px;line-height:36px}
.video{left:623px;top:79px;width:444px;height:235px;background:linear-gradient(#7a8aa6 0%,#b8a79a 45%,#5d4a3c 70%,#3d342c 100%)}
.play{position:absolute;left:200px;top:95px}
.testimonials{top:1168px;left:0;width:1200px;height:413px;background:var(--panel)}
.sec-title{font-size:23px;font-weight:600;color:var(--ink);text-align:center;position:absolute;width:1200px}
.testimonials .sec-title{top:72px}
.tcard{width:296px;top:132px}
.tbox{background:#fff;border:1px solid #e2e2e2;height:150px;padding:16px 20px 0 20px;position:relative}
.tbox q{display:block;font-size:12px;line-height:22px;color:#777;text-indent:38px;quotes:none}
.tbox .qmark{position:absolute;left:18px;top:8px;font-size:40px;color:#ccc;font-weight:800;line-height:1}
.tbox::after{content:"";position:absolute;right:0;bottom:-22px;border-left:36px solid transparent;border-top:22px solid #fff}
.tby{text-align:right;padding-right:46px;margin-top:16px;position:relative;line-height:1.3}
.tby b{font-size:13px;font-weight:600;color:var(--ink)}
.tby small{display:block;font-size:10px;color:var(--muted);font-weight:600}
.avatar{position:absolute;right:10px;top:-2px;width:34px;height:34px;background:#b7b2a8}
.tarrow{top:200px}
.press{top:1581px;left:0;width:1200px;height:339px}
.press h2{position:absolute;left:133px;top:76px;font-size:23px;font-weight:600;color:var(--ink)}
.viewmore{position:absolute;left:1013px;top:82px;background:var(--ink);color:#fff;font-size:8px;font-weight:700;padding:2px 7px}
.pcard{top:119px;width:217px;height:140px;background:var(--card);padding:20px 18px}
.pcard b{font-size:13px;font-weight:600;color:var(--ink);display:block;margin-bottom:6px}
.pcard p{font-size:12.5px;line-height:19px;color:#555}
.rule{top:1920px;left:0;width:1200px;height:2px;background:#e3e3e3}
.clients{top:1922px;left:0;width:1200px;height:247px}
.clients .sec-title{top:75px}
.logos{position:absolute;left:133px;top:132px;width:934px;display:flex;justify-content:space-between;align-items:center}
.logos span{font-size:20px;font-weight:700;color:#222;display:flex;align-items:center;gap:6px}
.logos i{width:14px;height:14px;border-radius:50%;background:#222;display:inline-block}
.footer{top:2169px;left:0;width:1200px;height:258px;background:var(--footer);color:#bbb}
.footer h4{font-size:20px;font-weight:600;color:#fff;position:absolute;top:50px}
.links{position:absolute;left:133px;top:94px;display:grid;grid-template-columns:145px 145px;font-size:11px;line-height:24px;color:#aaa}
.links div::before{content:"• "}
.contact{position:absolute;left:443px;top:92px;font-size:11px;line-height:24px;color:#aaa}
.contact div{display:flex;align-items:center;gap:10px}
.plan{position:absolute;left:730px;top:50px;width:337px}
.plan p{font-size:11.5px;color:#fff;line-height:1.4}
.fields{display:grid;grid-template-columns:160px 160px;gap:10px 7px;margin-top:14px}
.fields div{height:30px;background:#9a9a9a;color:#fff;font-size:12px;line-height:30px;padding-left:14px}
.plan .btn{width:72px;height:30px;line-height:30px;margin-top:14px;font-size:11px}
.bottom{top:2427px;left:0;width:1200px;height:66px;background:var(--footer-bottom)}
.bottom small{position:absolute;left:133px;top:26px;font-size:11px;color:#aaa}
.bottom .icons{position:absolute;right:133px;top:16px;display:flex;gap:8px}
.bottom .social{background:#888}
</style>
</head>
<body>

<header class="abs header">
  <div class="abs brand">
    <span class="brand-mark"></span>
    <span class="brand-name">COLE BRANDT</span>
  </div>
  <div class="abs connect">Connect with Cole Brandt
    <span class="social" aria-label="Social profile"></span><span class="social" aria-label="Social profile"></span><span class="social" aria-label="Social profile"></span><span class="social" aria-label="Social profile"></span>
  </div>
</header>

<nav class="abs nav">
  <ul>
    <li class="active">Home</li><li>About Cole Brandt</li><li>Motivational Speaker</li><li>Workshop Presenter</li><li>Author</li><li>Coaching</li><li>Blog</li><li>Online Courses</li><li>Contact Cole Brandt</li>
  </ul>
</nav>

<section class="abs hero">
  <div class="abs hero-photo" role="img" aria-label="Photo of a stressed man at an office desk holding his head in his hands"></div>
  <div class="abs arrow-tab" style="left:0"></div>
  <div class="abs arrow-tab" style="right:0"></div>
  <div class="abs sugar">
    <h2>Sugar Addiction</h2>
    <ul><li>Your bottom-line</li><li>Your Insurance Premiums</li><li>The health of your employees</li><li>The culture of your company</li></ul>
    <div class="foot">WITHOUT YOUR KNOWLEDGE OR CONSENT!</div>
  </div>
  <div class="abs hero-copy">
    <h1 class="hero-title">COLE BRANDT</h1>
    <div class="hero-sub">Sugar Addiction Expert, Holistic Health Expert, Author &amp; Speaker</div>
    <div class="hero-lead">YOUR HOLISTIC LIFESTYLE HACKER<br>LOSE YOUR MIND &amp; FIND YOUR HEALTH!</div>
    <div class="downloads">
      <div class="dl"><b>DOWNLOAD</b><span>Cole's Speaker One Sheet</span></div>
      <div class="dl"><b>DOWNLOAD</b><span>Cole's Media Sheet</span></div>
      <div class="dl"><b>DOWNLOAD</b><span>Cole's College Speaker One Sheet</span></div>
    </div>
    <p class="hero-text">For over 17 years, Cole Brandt has tirelessly helped executives, employees, and everyday people achieve lasting health and fitness by helping them "lose their minds." Using his unique 4-Quadrant Coaching System, speaking platform, and online training courses, Cole has helped hundreds of people shed their limiting beliefs, eat better, shed sugar addiction and transform their bodies and minds. Cole delights in helping people see through the self-deception of being "normal," and he invites his students to discover and accept the extraordinary people they truly are. If you are ready to transform physically, mentally, emotionally, and spiritually, it is time for you to meet Cole Brandt, your Holistic Health Hacker!</p>
    <span class="hero-cta">See How Cole Brandt Can Help You or Your Organization</span>
  </div>
</section>

<section class="abs optin">
  <div class="abs book" role="img" aria-label="Book cover of the author's book"></div>
  <h3>Learn WHY excuse making comes from an imbalanced body, mind, and soul and WHAT to do about it</h3>
  <form><div class="email">Email Address</div><div class="subscribe">SUBSCRIBE</div></form>
</section>

<section class="abs about">
  <h2>Etiam mattis augue vehicula odio</h2>
  <p>In addition to owning and operating Steadfast Fitness in Pine Hollow, Oregon, Cole Brandt is also a well-known public speaker and entrepreneur with an avid passion for health and fitness. His many areas of specialization include the science of sugar addiction, holistic health, and personal development. In addition to his professional research, Cole is also a multiple certified personal trainer and a Level III CORE Holistic Lifestyle Coach. He graduated from Westridge University in Exercise and Sports Science and has presented his FitPath Forward and Sugar</p>
  <div class="btn">LEARN MORE</div>
  <div class="abs video" role="img" aria-label="Video still of a man standing on a deck with mountains behind him">
    <svg class="play" width="44" height="44" viewBox="0 0 44 44"><circle cx="22" cy="22" r="21" fill="#fff"/><path d="M17 13 L31 22 L17 31 Z" fill="#222"/></svg>
  </div>
</section>

<section class="abs testimonials">
  <h2 class="sec-title">Testimonials</h2>
  <svg class="abs tarrow" style="left:48px" width="16" height="26" viewBox="0 0 16 26"><path d="M13 2 L3 13 L13 24" stroke="#777" stroke-width="4" fill="none"/></svg>
  <svg class="abs tarrow" style="left:1136px" width="16" height="26" viewBox="0 0 16 26"><path d="M3 2 L13 13 L3 24" stroke="#777" stroke-width="4" fill="none"/></svg>
  <div class="abs tcard" style="left:133px">
    <div class="tbox"><span class="qmark">“</span><q>Cole is a man of results. He helped me heal my painful knees, created a simple and effective system to improve my muscle balance and alignment. He sees the big picture, solving problems at the root cause...</q></div>
    <div class="tby"><b>Dana Whitfield,</b><small>Personal Coaching Client</small><span class="avatar" role="img" aria-label="Client portrait"></span></div>
  </div>
  <div class="abs tcard" style="left:450px">
    <div class="tbox"><span class="qmark">“</span><q>Cole has helped me change not only my physical state, but my mental state as well for the better. He has created a unique personal training business that get's involved with their clients and strives on...</q></div>
    <div class="tby"><b>Ravi Solano,</b><small>Personal coaching client of Cole Brandt</small><span class="avatar" role="img" aria-label="Client portrait"></span></div>
  </div>
  <div class="abs tcard" style="left:769px">
    <div class="tbox"><span class="qmark">“</span><q>I have known Cole for over 2 years and find him to be an exceptional person. Cole is an expert in personal fitness, health and mindset. He is honest in his business dealings. Cole has a wonderful and creative coaching...</q></div>
    <div class="tby"><b>Lena Marsh,</b><small>Personal coaching client of Cole Brandt</small><span class="avatar" role="img" aria-label="Client portrait"></span></div>
  </div>
</section>

<section class="abs press">
  <h2>Press Releases</h2>
  <span class="viewmore">VIEW MORE</span>
  <article class="abs pcard" style="left:133px"><b>8 DEC, 2017</b><p>Phasellus nisl est, condimentum vitae faucibus in, sollicitudin vel metus. Nunc sit amet consequat risus.</p></article>
  <article class="abs pcard" style="left:371px"><b>8 DEC, 2017</b><p>Praesent iaculis faucibus urna sit amet lacinia. Maecenas consequat justo enim, ac mattis massa</p></article>
  <article class="abs pcard" style="left:612px"><b>8 DEC, 2017</b><p>Fusce eget neque elit. Sed augue orci, elementum in magna congue, tincidunt vulputate erat.</p></article>
  <article class="abs pcard" style="left:851px"><b>8 DEC, 2017</b><p>Phasellus nisl est, condimentum vitae faucibus in, sollicitudin vel metus. Nunc sit amet consequat</p></article>
</section>

<div class="abs rule"></div>

<section class="abs clients">
  <h2 class="sec-title">Clients</h2>
  <div class="logos">
    <span><i></i>ROWAN</span><span>Halden</span><span>Vortex</span><span>OAKLINE</span><span>Kestrel</span><span>LUMA</span><span>RIVERTON</span>
  </div>
</section>

<footer class="abs footer">
  <h4 style="left:133px">Links</h4>
  <div class="links">
    <div>Home</div><div>Coaching</div>
    <div>About Cole Brandt</div><div>Blog</div>
    <div>Motivational Speaker</div><div>Online Courses</div>
    <div>Workshop Presenter</div><div>Contact Cole Brandt</div>
    <div>Author</div>
  </div>
  <h4 style="left:443px">Contact Info</h4>
  <div class="contact">
    <div><svg width="9" height="12" viewBox="0 0 9 12"><path d="M4.5 0 A4.5 4.5 0 0 1 9 4.5 C9 7 4.5 12 4.5 12 C4.5 12 0 7 0 4.5 A4.5 4.5 0 0 1 4.5 0Z" fill="#aaa"/><circle cx="4.5" cy="4.5" r="1.6" fill="#2b2b2b"/></svg>24 Building name, Street name, City - Zipcode</div>
    <div><svg width="10" height="10" viewBox="0 0 10 10"><path d="M2 0 L4 3 L3 4 C4 6 5 7 6 7 L7 6 L10 8 L8.5 10 C4 10 0 6 0 1.5Z" fill="#aaa"/></svg>555 014 2290</div>
    <div><svg width="10" height="8" viewBox="0 0 10 8"><rect width="10" height="8" fill="#aaa"/><path d="M0 0 L5 4.5 L10 0" stroke="#2b2b2b" fill="none"/></svg>info@colebrandt.example</div>
  </div>
  <div class="plan">
    <p>Become a Holistic Health Hacker and receive a FREE 30-Day Meal Plan crafted by Cole!</p>
    <div class="fields"><div>Name</div><div>Email</div><div>Phone</div><div>Message</div></div>
    <div class="btn">SUBMIT</div>
  </div>
</footer>

<div class="abs bottom">
  <small>Copyright © 2017 Cole Brandt. All rights reserved.</small>
  <div class="icons"><span class="social" aria-label="Social profile"></span><span class="social" aria-label="Social profile"></span><span class="social" aria-label="Social profile"></span><span class="social" aria-label="Social profile"></span></div>
</div>

</body>
</html>
```